VMR business card

Need a business card for a company that provides instructional design and elearning development services. The website is here: http://vantmoro.studio/

I'm attaching a current logo, as well as the old business card design. While I like to keep it clean, the old design is too simplistic for my liking. The only idea I want to reuse from the old design is placing industry jargon on the back of the card, just need a better way to present it. But if you have other ideas for the back--feel free to experiment.

Please use the colors complementary to the color we have on the website. Thank you!

```html
<!DOCTYPE html>
<html lang="en">
<head>
<meta charset="utf-8">
<title>VMR business card</title>
<link rel="stylesheet" href="https://fonts.googleapis.com/css2?family=Ubuntu:wght@400;500&family=Open+Sans:wght@600&family=PT+Sans+Narrow&display=swap">
<style>
  :root {
    --backdrop: #8c8d8f;
    --paper: #f2f2f3;
    --teal: #1a9e9c;
    --gold: #b9ab6b;
    --ink: #3d3d3f;
    --rule: #9a9a9c;
    --back-text: #e9f4f3;
    --back-rule: rgba(233, 244, 243, 0.75);
  }
  * { margin: 0; padding: 0; box-sizing: border-box; }
  html, body { width: 1105px; height: 1200px; overflow: hidden; }
  body { background: var(--backdrop); position: relative; }

  .card {
    position: absolute;
    left: 180px;
    width: 746px;
    height: 425px;
    overflow: hidden;
  }
  .card--front { top: 120px; background: var(--paper); font-family: "Ubuntu", sans-serif; }
  .card--back { top: 636px; background: var(--teal); }

  /* Front */
  .brand {
    position: absolute;
    left: 52px;
    top: 186px;
    display: flex;
    align-items: center;
    gap: 14px;
  }
  .brand__dot { width: 34px; height: 34px; border-radius: 50%; background: var(--teal); }
  .brand__name {
    font-family: "Ubuntu", sans-serif;
    font-weight: 500;
    font-size: 56px;
    line-height: 1;
    letter-spacing: 2px;
    color: var(--gold);
  }
  .front-rule {
    position: absolute;
    left: 359px;
    top: 132px;
    width: 1px;
    height: 162px;
    background: var(--rule);
  }
  .contact { position: absolute; left: 388px; top: 128px; }
  .contact__name { font-size: 24px; color: var(--teal); font-weight: 400; line-height: 1.2; }
  .contact__role { font-size: 17px; color: var(--gold); margin-top: 3px; line-height: 1.2; }
  .contact__list { list-style: none; margin-top: 20px; }
  .contact__item {
    display: flex;
    align-items: center;
    gap: 10px;
    font-size: 18px;
    color: var(--ink);
    height: 29px;
  }
  .contact__icon { width: 17px; height: 17px; flex: none; }

  /* Back */
  .prompt {
    font-family: "Open Sans", sans-serif;
    font-weight: 600;
    color: var(--back-text);
  }
  .prompt__line {
    position: absolute;
    left: 21px;
    display: block;
    font-size: 76px;
    line-height: 1;
    letter-spacing: 3px;
    white-space: nowrap;
  }
  .prompt__line--how { top: 27px; }
  .prompt__line--can { top: 120px; }
  .prompt__line--we { top: 190px; font-size: 102px; letter-spacing: 14px; }
  .prompt__line--help { top: 328px; letter-spacing: 1px; }
  .back-rule {
    position: absolute;
    left: 257px;
    top: 34px;
    width: 2px;
    height: 365px;
    background: var(--back-rule);
  }
  .topics {
    position: absolute;
    left: 279px;
    top: 27px;
    list-style: none;
    font-family: "PT Sans Narrow", sans-serif;
    font-size: 50px;
    line-height: 63.7px;
    color: var(--back-text);
    white-space: nowrap;
    transform: scaleX(0.865);
    transform-origin: left top;
  }
</style>
</head>
<body>
  <section class="card card--front">
    <div class="brand">
      <span class="brand__dot"></span>
      <span class="brand__name">VMR</span>
    </div>
    <div class="front-rule"></div>
    <div class="contact">
      <p class="contact__name">Daria Kessington</p>
      <p class="contact__role">CEO/Founder</p>
      <ul class="contact__list">
        <li class="contact__item">
          <svg class="contact__icon" viewBox="0 0 24 24"><path fill="#1a9e9c" d="M6.6 10.8a15.2 15.2 0 0 0 6.6 6.6l2.2-2.2a1 1 0 0 1 1-.25 11.4 11.4 0 0 0 3.6.57 1 1 0 0 1 1 1V20a1 1 0 0 1-1 1A17 17 0 0 1 3 4a1 1 0 0 1 1-1h3.5a1 1 0 0 1 1 1c0 1.25.2 2.45.57 3.57a1 1 0 0 1-.25 1z"/></svg>
          555-014-2287
        </li>
        <li class="contact__item">
          <svg class="contact__icon" viewBox="0 0 24 24"><rect x="2" y="5" width="20" height="14" rx="1" fill="#1a9e9c"/><path d="M3 6l9 7 9-7" fill="none" stroke="#f2f2f3" stroke-width="1.6"/></svg>
          dkessington@vantmoro.studio
        </li>
        <li class="contact__item">
          <svg class="contact__icon" viewBox="0 0 24 24"><circle cx="12" cy="12" r="10" fill="#1a9e9c"/><path d="M2 12h20M12 2c3 3 3 17 0 20M12 2c-3 3-3 17 0 20" fill="none" stroke="#f2f2f3" stroke-width="1.3"/></svg>
          www.vantmoro.studio
        </li>
      </ul>
    </div>
  </section>

  <section class="card card--back">
    <h2 class="prompt">
      <span class="prompt__line prompt__line--how">HOW</span>
      <span class="prompt__line prompt__line--can">CAN</span>
      <span class="prompt__line prompt__line--we">WE</span>
      <span class="prompt__line prompt__line--help">HELP?</span>
    </h2>
    <div class="back-rule"></div>
    <ul class="topics">
      <li>MOBILE LEARNING SCORM</li>
      <li>INSTRUCTIONAL DESIGN LMS</li>
      <li>MOOCS ELEARNING HTML5</li>
      <li>ADULT LEARNING THEORY</li>
      <li>GAMIFICATION CLASSROOM</li>
      <li>XAPI BLENDED LEARNING</li>
    </ul>
  </section>
</body>
</html>
```